Website update for Mobile lighting company

We are looking to get a fresh look to our website and update it with some new products and services we are just starting to offer. We host there website through go daddy and use there website builder so we would like comparable files. The pages we would want are:
Home page
RUNE (one of our light tower units)
KT75 (one of our light tower units)
KT45 (one of our light tower units)
KT20 (one of our light tower units)
Service Page (would describe different serves we provide)
Contact Page with a google map
We would like to stick with our company colours and keep it clean and modern looking. Current website is www.brindlepower.ca

```html
<!DOCTYPE html>
<html lang="en">
<head>
<meta charset="utf-8">
<title>Brindle Power Services Corp.</title>
<link href="https://fonts.googleapis.com/css2?family=Open+Sans:wght@400;600;700&display=swap" rel="stylesheet">
<style>
:root{
  --lime:#cdc932;
  --lime-text:#c2c22a;
  --ink:#1b1b1b;
  --nav:#231e1b;
  --body:#2a2a2a;
  --footer:#050505;
  --footer-text:#8a8a8a;
}
*{margin:0;padding:0;box-sizing:border-box}
html,body{width:843px;height:1200px;overflow:hidden}
body{font-family:"Open Sans",sans-serif;color:var(--body);background:#fff;position:relative}
.abs{position:absolute}
.top-band{left:0;top:0;width:843px;height:405px;background:linear-gradient(180deg,#f0f0f0,#e6e6e6);border-bottom:2px solid #dcdcdc}
.brand{left:103px;top:24px;display:flex;align-items:center;gap:8px}
.brand-mark{width:26px;height:26px;border-radius:50%;background:var(--lime)}
.brand-name{font-size:22px;font-weight:600;color:var(--lime-text);letter-spacing:.5px}
.social{display:flex;gap:9px}
.social span{width:9px;height:9px;border-radius:50%;background:#6a6a6a;display:block}
.social.header{left:655px;top:27px}
.phones{left:462px;top:53px;font-size:8.5px;color:#555;display:flex;gap:14px}
.phones svg,.contact svg{vertical-align:-2px;margin-right:5px}
.nav{left:102px;top:85px;width:639px;height:39px;background:var(--nav);border-top:5px solid var(--lime);border-radius:4px 4px 0 0;display:flex;padding-left:24px}
.nav a{color:#fff;text-decoration:none;font-size:9.5px;font-weight:600;height:34px;line-height:34px;padding:0 15px;border-right:1px solid #3a3431}
.nav a.active{background:var(--lime);color:var(--ink);padding:0 8px;border:none}
.nav a:last-child{border:none}
.hero{left:102px;top:124px;width:639px;height:249px;background:linear-gradient(100deg,#050507 0,#08080b 40%,#25252a 62%,#3c3c40 72%,#0b0b0e 100%)}
.hero-title{left:23px;top:120px;font-size:20px;color:#fff}
.hero-text{left:23px;top:152px;width:210px;font-size:8.5px;line-height:16px;color:#fff;font-weight:600}
.shadow{height:12px;background:radial-gradient(ellipse at 50% 0,rgba(0,0,0,.35),transparent 70%)}
.dots{left:397px;top:388px;display:flex;gap:3px}
.dots span{width:7px;height:7px;border-radius:50%;border:1px solid #999;background:#fff}
.dots span.on{background:var(--lime);border-color:var(--lime)}
h2{font-weight:400;font-size:16.5px;color:var(--ink)}
.para{font-size:8.5px;line-height:16px;color:#333}
.btn{display:block;width:68px;height:29px;background:linear-gradient(#3b3b3b,#151515);color:#fff;font-size:9px;text-align:center;line-height:29px;border-radius:2px}
.tabs{left:504px;top:458px;width:237px;height:25px;border:1px solid #ccc;display:flex;font-size:9.5px}
.tabs span{padding:0 13px;line-height:23px;color:#666;border-right:1px solid #ccc}
.tabs span.on{color:var(--ink);font-weight:600}
.solution{left:101px;top:634px;width:640px;height:336px;background:var(--lime);border-left:2px solid #b9b52a}
.feature{width:220px}
.feature h3{font-size:13.5px;font-weight:400;color:var(--ink);display:flex;align-items:center;gap:8px;height:28px}
.feature p{font-size:8.5px;line-height:16px;color:#222;margin-top:10px;width:200px}
.feature b{font-size:8.5px;font-weight:600;color:#111}
.footer{left:0;top:1012px;width:843px;height:188px;background:var(--footer)}
.footer h4{font-size:12.5px;font-weight:400;color:var(--lime-text)}
.contact{list-style:none;font-size:8.5px;color:var(--footer-text)}
.contact li{height:20px}
.copy{left:0;top:1177px;width:843px;text-align:center;font-size:8px;color:#888}
</style>
</head>
<body>
<div class="abs top-band"></div>

<header>
  <div class="abs brand"><span class="brand-mark"></span><span class="brand-name">Brindle Power Services Corp.</span></div>
  <div class="abs social header"><span></span><span></span><span></span><span></span><span></span></div>
  <div class="abs phones">
    <span><svg width="8" height="8" viewBox="0 0 10 10"><path d="M2 0l2 2-1 2 3 3 2-1 2 2-2 2C4 10 0 6 0 2z" fill="#cdc932"/></svg>Colin Telephone: 7805550148</span>
    <span><svg width="8" height="8" viewBox="0 0 10 10"><path d="M2 0l2 2-1 2 3 3 2-1 2 2-2 2C4 10 0 6 0 2z" fill="#cdc932"/></svg>Reid Telephone: 4035550173</span>
  </div>
  <nav class="abs nav">
    <a class="active">Home</a><a>RUNE</a><a>KT75</a><a>KT45</a><a>KT20</a><a>Services</a><a>Contact us</a>
  </nav>
</header>

<section class="abs hero" role="img" aria-label="Photograph of a light tower unit working at night">
  <div class="abs hero-title">Environmental Benefits</div>
  <p class="abs hero-text">Lorem Ipsum. aliquet. Aenean sollicitudin, lorem quis bibendum auctor,</p>
</section>
<div class="abs shadow" style="left:180px;top:373px;width:480px"></div>
<div class="abs dots"><span class="on"></span><span></span><span></span><span></span><span></span></div>

<section class="abs" style="left:103px;top:426px;width:340px">
  <h2>About RUNE</h2>
  <p class="para" style="margin-top:12px">Lorem Ipsum. aliquet. Aenean sollicitudin, lorem quis bibendum auctor, nisi elit consequat ipsum, nec sagittis sem nibh id elit. Duis sed odio sit amet nibh vulputate cursus a sit amet mauris.</p>
  <p class="para" style="margin-top:16px">Morbi accumsan ipsum velit. Nam nec tellus a odio tincidunt auctor a ornare odiod non&nbsp; mauris vitae erat consequat.</p>
</section>
<span class="abs btn" style="left:103px;top:570px">READ MORE</span>

<section class="abs" style="left:503px;top:424px;width:238px">
  <h2>How It Works</h2>
</section>
<div class="abs tabs"><span class="on">Step1</span><span>Step2</span><span>Step3</span></div>
<div class="abs" style="left:505px;top:492px;width:236px">
  <p style="font-size:9.5px;font-weight:600;color:var(--ink)">Proin gravida nibh vel velit auctor aliquet</p>
  <p class="para" style="margin-top:9px">Lorem Ipsum. aliquet. Aenean sollicitudin, lorem quis bibendum auctor, nisi elit consequat ipsum, nec sagittis sem nibh id elit.</p>
</div>
<span class="abs btn" style="left:504px;top:570px">READ MORE</span>

<section class="abs solution">
  <h2 class="abs" style="left:24px;top:14px">Our Solution</h2>
  <div class="abs feature" style="left:63px;top:72px">
    <h3><svg width="30" height="26" viewBox="0 0 30 26"><path d="M15 0v5M9 7l6-3 6 3" stroke="#111" fill="none" stroke-width="1.5"/><rect x="1" y="8" width="28" height="16" rx="1" fill="#111"/><path d="M7 11v10M12 11v10M18 11v10M23 11v10" stroke="#cdc932" stroke-width="1.5"/></svg>Self Contained Unit</h3>
    <p>Lorem Ipsum. aliquet. Aenean sollicitudin, lorem quis bibendum auctor, nisi elit.</p><b>Read More</b>
  </div>
  <div class="abs feature" style="left:380px;top:72px">
    <h3><svg width="30" height="28" viewBox="0 0 30 28"><path d="M15 2l6 9h-12zM4 26l5-10 6 9zM26 26l-12-1 6-9z" fill="#111"/></svg>Environmental Benefits</h3>
    <p>Lorem Ipsum. aliquet. Aenean sollicitudin, lorem quis bibendum auctor, nisi elit.</p><b>Read More</b>
  </div>
  <div class="abs feature" style="left:63px;top:218px">
    <h3><svg width="30" height="26" viewBox="0 0 30 26"><circle cx="15" cy="10" r="6" fill="none" stroke="#111" stroke-width="4" stroke-dasharray="3 2"/><circle cx="15" cy="10" r="5" fill="#111"/><circle cx="15" cy="10" r="2" fill="#cdc932"/><path d="M3 19v5h24v-5" stroke="#111" stroke-width="2" fill="none"/></svg>Easy To Install</h3>
    <p>Lorem Ipsum. aliquet. Aenean sollicitudin, lorem quis bibendum auctor, nisi elit.</p><b>Read More</b>
  </div>
  <div class="abs feature" style="left:380px;top:218px">
    <h3><svg width="30" height="28" viewBox="0 0 30 28"><path d="M9 12V8a6 6 0 0 1 12 0v4" stroke="#111" stroke-width="3" fill="none"/><rect x="6" y="12" width="18" height="15" rx="2" fill="#111"/><circle cx="15" cy="19" r="2" fill="#cdc932"/></svg>Better Overall Safety</h3>
    <p>Lorem Ipsum. aliquet. Aenean sollicitudin, lorem quis bibendum auctor, nisi elit.</p><b>Read More</b>
  </div>
</section>
<div class="abs shadow" style="left:180px;top:970px;width:480px"></div>

<footer class="abs footer">
  <h4 class="abs" style="left:125px;top:20px">Contact Detail</h4>
  <ul class="abs contact" style="left:127px;top:54px">
    <li><svg width="9" height="9" viewBox="0 0 10 10"><path d="M2 0l2 2-1 2 3 3 2-1 2 2-2 2C4 10 0 6 0 2z" fill="#cdc932"/></svg>Colin Telephone: 7805550148</li>
    <li><svg width="9" height="9" viewBox="0 0 10 10"><path d="M2 0l2 2-1 2 3 3 2-1 2 2-2 2C4 10 0 6 0 2z" fill="#cdc932"/></svg>Reid Telephone: 4035550173</li>
    <li><svg width="9" height="7" viewBox="0 0 10 7"><rect width="10" height="7" fill="#cdc932"/><path d="M0 0l5 4 5-4" stroke="#050505" fill="none"/></svg>Email: colin@brindlepowerservices.ca</li>
    <li><svg width="9" height="7" viewBox="0 0 10 7"><rect width="10" height="7" fill="#cdc932"/><path d="M0 0l5 4 5-4" stroke="#050505" fill="none"/></svg>Email: reid@brindlepowerservices.ca</li>
  </ul>
  <div class="abs" style="left:445px;top:41px;width:1px;height:95px;background:#222"></div>
  <h4 class="abs" style="left:576px;top:16px">Get in Touch</h4>
  <div class="abs social" style="left:576px;top:62px"><span></span><span></span><span></span><span></span><span></span></div>
  <div class="abs" style="left:0;top:151px;width:843px;height:1px;background:#1c1c1c"></div>
</footer>
<p class="abs copy">©Copyright 2014&nbsp;&nbsp; BRINDLE POWER SERVICES CORP. . All rights reserved</p>
</body>
</html>
```